Need Wordpress Blog Designed

I have just started a blog (www.velvetpantrybites.com), but I don't have a design background to make it look good.

Specifically I would like to add:

Top – Home, About, Contact

Sidebar – Categories, Blog Roll, plain square, plain square, Top Post, Tag Cloud, Recent Post, area to upload a video.

I would also like to normalize the font and the format and add cool buttons for links like the more button.

The colors chosen can be any of the colors used in the logo.

Other recommendations and changes are welcome as well.

Requirements
Must have
• Logo

```html
<!DOCTYPE html>
<html lang="en">
<head>
<meta charset="utf-8">
<title>Velvet Pantry Bites</title>
<link rel="stylesheet" href="https://fonts.googleapis.com/css2?family=Arimo:wght@400;700&family=Gelasio&display=swap">
<style>
:root{
  --brown-dark:#2b160c;
  --brown:#4a2614;
  --brown-mid:#6b3a1f;
  --pink:#e0306e;
  --yellow:#f4ee8c;
  --yellow-head:#e8df78;
  --text:#222;
  --muted:#555;
  --white:#fff;
}
*{margin:0;padding:0;box-sizing:border-box}
html,body{width:828px;height:1200px;overflow:hidden;background:var(--white)}
body{position:relative;font-family:Arimo,Arial,sans-serif;color:var(--text)}
.abs{position:absolute}
.tagline{left:46px;top:17px;font-size:11px;font-weight:700;color:#3a2a20}
.brand{left:46px;top:42px;font-size:30px;font-weight:700;color:var(--brown)}
.brand-dot{left:46px;top:52px;display:none}
.search{left:390px;top:72px;width:164px;height:18px;border:1px solid #8a8a8a;border-radius:2px;font-size:10px;font-weight:700;text-align:right;padding:3px 4px 0 0}
.nav a{position:absolute;top:68px;height:24px;border-radius:5px;color:var(--white);font-size:14px;text-decoration:none;text-align:center;line-height:24px;background:var(--brown-dark)}
.nav .home{left:574px;width:65px;background:var(--pink)}
.nav .about{left:644px;width:62px}
.nav .contact{left:710px;width:71px}
.hero-band{left:0;top:100px;width:828px;height:360px;background:linear-gradient(135deg,#3a1c0e,#6b3a1f 40%,#2b140a 70%,#5a3018)}
.hero-panel{left:34px;top:140px;width:758px;height:280px;background:var(--white)}
.hero-title{left:62px;top:238px;font-size:25px;font-weight:700;color:var(--brown-dark)}
.hero-title span{color:var(--pink)}
.hero-copy{left:62px;top:270px;width:345px;font-size:16px;line-height:22px;color:var(--brown-dark)}
.hero-photo{left:404px;top:145px;width:384px;height:267px;background:radial-gradient(circle at 45% 55%,#4a2a1a,#8a5a3a 45%,#efe9e4 75%)}
h2{font-family:Gelasio,Georgia,serif;font-weight:400;color:var(--brown-dark)}
.about-h{left:34px;top:474px;font-size:26px}
.about-copy{left:34px;top:516px;width:486px;font-size:11.5px;line-height:17px}
.more-link{font-size:11px;color:#3a2a20;letter-spacing:.5px}
.video-h{left:35px;top:650px;font-size:20px}
.player{left:34px;top:685px;width:324px;height:225px;background:#000}
.video-copy{left:382px;top:720px;width:145px;font-size:11px;line-height:17px}
.upload-btn{left:377px;top:802px;width:141px;height:54px;border-radius:8px;background:linear-gradient(#6b3a1f,#2b160c);color:var(--white);font-size:17px;line-height:17px;padding:10px 0 0 63px}
.cat-h{left:575px;top:481px;font-size:20px}
.rule{border-top:1px dashed #999}
.cats{left:581px;top:519px;list-style:none;font-size:10px}
.cats li{height:25px}
.recent{left:562px;top:685px;width:229px;height:227px;background:var(--yellow);border-radius:4px;overflow:hidden}
.recent-head{height:33px;background:var(--yellow-head);font-family:Gelasio,Georgia,serif;font-size:20px;padding:5px 0 0 14px;color:var(--brown-dark)}
.post{position:absolute;left:15px;width:200px;font-size:10px;line-height:16px;color:#333}
.post b{display:block;color:var(--text)}
.recent-more{position:absolute;right:1px;bottom:2px;background:var(--white);font-size:11px;padding:2px 9px;border-radius:3px}
.top-h{left:48px;top:928px;font-size:19px}
.top-post{left:50px;width:390px;font-size:10px;line-height:16px;color:#333}
.top-post b{display:block;color:var(--text)}
.cloud{left:512px;top:937px;width:280px;height:166px;border:1px solid #ccc;padding:6px}
.cloud div{width:100%;height:100%;background:linear-gradient(135deg,#e8e8e8,#bcbcbc 50%,#f2f2f2)}
.footer{left:0;top:1123px;width:828px;height:58px;background:linear-gradient(135deg,#2b140a,#5a3018 50%,#2b140a)}
.footer-nav{left:42px;top:1140px;font-size:11px;color:var(--white)}
.footer-nav span{margin-right:12px}
.social{top:1137px;width:20px;height:20px;border-radius:4px;background:#4a90c8}
.copyright{left:0;top:1181px;width:828px;height:19px;background:var(--brown-dark);color:#ddd;font-size:10px;text-align:center;line-height:19px}
</style>
</head>
<body>
<header>
  <p class="abs tagline">Your source for positive news stories in the black community</p>
  <p class="abs brand">Velvet Pantry Bites</p>
  <div class="abs search">SEARCH</div>
  <nav class="nav"><a class="home">Home</a><a class="about">About</a><a class="contact">Contact</a></nav>
</header>

<section>
  <div class="abs hero-band" role="img" aria-label="Swirling melted chocolate backdrop"></div>
  <div class="abs hero-panel"></div>
  <h1 class="abs hero-title">Velvet <span>Pantry</span> Bites</h1>
  <p class="abs hero-copy">Lorem Ipsum is simply dummy text of the printing and typesetting industry. Lorem Ipsum has been the industry's standard dummy text ever since</p>
  <div class="abs hero-photo" role="img" aria-label="Chocolate bar surrounded by coffee beans"></div>
</section>

<main>
  <h2 class="abs about-h">About</h2>
  <div class="abs about-copy">
    <p>This is an example page. It's different from a blog post because it will stay in one place and will show up in your site navigation (in most themes). Most people start with an About page that introduces them to potential site visitors. It might say something like this:</p>
    <p style="margin-top:17px">Hi there! I'm a bike messenger by day, aspiring actor by night, and this is my blog. I live in Los Angeles, have a great dog named Jack, and I like piña coladas. (And gettin' caught in the rain.)</p>
  </div>
  <span class="abs more-link" style="left:462px;top:634px">Read more</span>

  <h2 class="abs video-h">Upload Videos</h2>
  <svg class="abs player" viewBox="0 0 324 225" aria-label="Video player">
    <rect width="324" height="225" fill="#000"/>
    <circle cx="162" cy="103" r="6" fill="none" stroke="#777" stroke-width="2" stroke-dasharray="3 2"/>
    <rect y="204" width="324" height="21" fill="#1e1e1e"/>
    <rect y="203" width="324" height="2" fill="#444"/>
    <circle cx="4" cy="204" r="4" fill="#ccc"/>
    <path d="M12 210l7 4-7 4z" fill="#999"/>
    <path d="M34 212h3l4-3v10l-4-3h-3z" fill="#999"/>
    <text x="52" y="217" font-size="6" fill="#aaa" font-family="Arimo,Arial,sans-serif">0:00 / 4:26</text>
    <text x="262" y="217" font-size="6" fill="#888" font-family="Arimo,Arial,sans-serif">360p</text>
    <rect x="281" y="208" width="12" height="12" fill="#444"/>
    <rect x="296" y="208" width="10" height="12" fill="#333"/>
    <rect x="310" y="208" width="12" height="12" fill="#555"/>
  </svg>
  <p class="abs video-copy">Lorem Ipsum is simply dummy text of the printing and typesetting industry. Lorem Ipsum is simply dummy</p>
  <div class="abs upload-btn">
    <svg class="abs" style="left:18px;top:12px" width="32" height="32" viewBox="0 0 32 32" aria-hidden="true">
      <circle cx="16" cy="16" r="15" fill="#e8eef5"/><circle cx="16" cy="16" r="11" fill="#3b7fc4"/><path d="M13 10l9 6-9 6z" fill="#fff"/>
    </svg>
    Upload<br>video
  </div>

  <h2 class="abs top-h">Top Post</h2>
  <div class="abs top-post" style="top:963px">
    <b>Posted on January 7, 2012</b>
    <b>Lena Marlow, DJ Royce's daughter, gets new show on Brightside TV</b>
    It looks like DJ Royce's children are determined to be stars like their dad. Lena Marlow<br>The rapper's daughter, Lena Marlow, will be hitting living rooms .....
  </div>
  <div class="abs rule" style="left:50px;top:1028px;width:380px"></div>
  <div class="abs top-post" style="top:1032px">
    <b>Posted on January 7, 2012</b>
    <b>Black Fraternities Form Hale Super PAC</b>
    Another factor making 2012 politically historic? It marks the first presidential election with super PACs.
  </div>
  <span class="abs more-link" style="left:402px;top:1090px">Read more</span>
</main>

<aside>
  <h2 class="abs cat-h">Categories</h2>
  <div class="abs rule" style="left:575px;top:507px;width:203px"></div>
  <ul class="abs cats">
    <li>Lorem Ipsum is simply</li><li>Lorem Ipsum is simply dummy</li><li>Lorem Ipsum is</li>
    <li>Lorem Ipsum is simply</li><li>Lorem Ipsum</li><li>Lorem Ipsum is simply dummy</li>
  </ul>
  <span class="abs more-link" style="left:708px;top:667px">more categories</span>

  <div class="abs recent">
    <div class="recent-head">Recent Posts</div>
    <div class="post" style="top:40px"><b>Posted on January 7, 2012</b>Black Woman named to head Women in Flight Board of Directors ...</div>
    <div class="abs rule" style="left:15px;top:97px;width:200px"></div>
    <div class="post" style="top:102px"><b>Posted on January 7, 2012</b>Lena Marlow, DJ Royce's daughter, gets new show on Brightside TV</div>
    <div class="abs rule" style="left:15px;top:159px;width:200px"></div>
    <div class="post" style="top:164px"><b>Posted on January 7, 2012</b>Black Fraternities Form Hale Super PAC</div>
    <span class="recent-more">more</span>
  </div>

  <div class="abs cloud"><div role="img" aria-label="Tag cloud of blogging keywords"></div></div>
</aside>

<footer>
  <div class="abs footer" role="img" aria-label="Melted chocolate backdrop"></div>
  <p class="abs footer-nav"><span>Home</span><span>About</span><span>Contact</span></p>
  <div class="abs social" style="left:698px" aria-label="Social link"></div>
  <div class="abs social" style="left:726px;background:#3b5ea8" aria-label="Social link"></div>
  <div class="abs social" style="left:754px;background:#f07a20" aria-label="Social link"></div>
  <p class="abs copyright">All rights Reserved, 2012 Velvet Pantry Bites</p>
</footer>
</body>
</html>
```